Homepage für Immobilienmakler
Zielgruppe
Wir sind ein neuer und junger Immobilienmakler. Wir wollen moderne und neue Wege gehen. Damit meinen wir, extrem modern und auffallend professionell.
Unsere Immobilien sind von Anlegerwohnungen über Häuser bis hin zu Gewerbeimmobilien
Unsere Zielgruppe ist von jung bis alt quer durch.
Aufgabenstellung
Homepagegestalltung für unsere Immobilienmaklerei.
Persönlich gefällt mir sehr gut das schwarz-weiß, jedoch wirkt das dann eher zu dunkel nehme ich mal an. Sonst würde mir die Homepage in grün, wie die Farbe im Logo, gut gefallen. Eventuell in weißer Schrift. ABER, ICH ÜBERLASSE EUCH DIE DESIGNSFARBEN.
Mir hätte dieses Design sehr gut gefallen, eventuelll könnt ihr dieses umgestallten:
http://vorlagenhain.example/item/auto-dealer-car-dealer-html-template/full_screen_preview/7719034
Kein muss, wenn ihr etwas besseres habt, dann bin ich auch froh ;)
Eventuell etwas mit Bewegung auf der Homepage oder so wäre auch gut.
Unsere Homepage hat die Domain:
wohnraum-kontor.example
Das Foto von mir sollte auf der Homepage eingebaut werden.
Auf der Homepage sollen die Immobilien, die wir verkaufen und vermieten angeführt werden. Zudem sollte ersichtlich sein, dass wir Immobilien suchen, um diese zu verkaufen oder zu vermieten.

```html
<!DOCTYPE html>
<html lang="de">
<head>
<meta charset="utf-8">
<title>Wohnraum Kontor</title>
<link href="https://fonts.googleapis.com/css2?family=Ubuntu:wght@300;400;500;700&display=swap" rel="stylesheet">
<style>
  :root {
    --black: #1b1b1b;
    --green: #3cb54a;
    --blue: #29a8e0;
    --grey-band: #e8e8e8;
    --light-tab: #efefef;
    --ink: #222;
    --white: #ffffff;
  }
  * { margin: 0; padding: 0; box-sizing: border-box; }
  html, body { width: 971px; height: 1200px; overflow: hidden; background: var(--white); }
  body { position: relative; font-family: "Ubuntu", sans-serif; }

  .site-header { position: absolute; left: 0; top: 0; width: 971px; height: 60px; background: var(--black); }
  .brand { position: absolute; left: 191px; top: 8px; font-size: 38px; font-weight: 700; color: var(--green); letter-spacing: -0.5px; }
  .social { position: absolute; top: 17px; width: 28px; height: 28px; border: 2px solid var(--white); border-radius: 50%; }
  .social--a { left: 723px; }
  .social--b { left: 761px; }

  .hero { position: absolute; left: 0; top: 60px; width: 971px; height: 447px;
    background: linear-gradient(180deg, #cfe0f2 0%, #a9c7e6 30%, #8fae7a 52%, #5f7f3a 62%, #4d6d2a 100%); }
  .main-nav { position: absolute; left: 0; top: 61px; height: 24px; }
  .main-nav a { position: absolute; top: 0; height: 24px; line-height: 24px; font-size: 9px; font-weight: 700; color: var(--black); text-decoration: none; transform: translateX(-50%); white-space: nowrap; }
  .main-nav a.is-active { background: var(--black); color: var(--white); padding: 0 8px; }
  .hero-title { position: absolute; left: 494px; top: 100px; font-size: 34px; font-weight: 400; color: var(--ink); }

  .grey-band { position: absolute; left: 0; top: 507px; width: 971px; height: 396px; background: var(--grey-band); }

  .tab { position: absolute; top: 449px; width: 187px; height: 27px; padding-left: 14px; line-height: 25px; font-size: 14px; font-weight: 500; }
  .tab--buy { left: 192px; background: var(--blue); color: var(--white); }
  .tab--rent { left: 392px; background: var(--green); color: var(--white); }
  .tab--offer { left: 589px; background: var(--light-tab); color: var(--ink); }
  .caret { position: absolute; right: 10px; top: 11px; border-left: 5px solid transparent; border-right: 5px solid transparent; border-top: 5px solid currentColor; }

  .search-panel { position: absolute; left: 192px; top: 476px; width: 187px; height: 315px; background: var(--white); box-shadow: 0 1px 3px rgba(0,0,0,.15); }
  .search-field { position: absolute; left: 15px; right: 10px; font-size: 14px; font-weight: 500; color: var(--blue); }
  .search-field .caret { color: var(--black); top: 6px; right: 0; }
  .search-submit { position: absolute; left: 0; bottom: 0; width: 187px; height: 26px; background: var(--blue); color: var(--white); font-size: 14px; font-weight: 500; padding-left: 15px; line-height: 26px; }
  .search-submit .pin { position: absolute; right: 8px; top: -4px; width: 20px; height: 20px; border: 2px solid var(--white); border-radius: 50%; }

  .phone { position: absolute; left: 193px; top: 832px; font-size: 39px; font-weight: 700; color: var(--green); letter-spacing: 1px; }
  .contact-copy { position: absolute; left: 193px; top: 910px; font-size: 22px; font-weight: 300; line-height: 29px; color: var(--green); }

  .agent-photo { position: absolute; left: 621px; top: 695px; width: 206px; height: 493px;
    background: linear-gradient(180deg, #8a6c58 0%, #b48f7a 18%, #f2f2f2 30%, #e6e6e6 70%, #2e3038 85%, #25272d 100%);
    border-radius: 80px 80px 8px 8px; }
</style>
</head>
<body>
  <header class="site-header">
    <div class="brand">Wohnraum Kontor</div>
    <span class="social social--a" aria-label="Soziales Netzwerk"></span>
    <span class="social social--b" aria-label="Soziales Netzwerk"></span>
  </header>

  <section class="hero" role="img" aria-label="Foto einer grünen Wiese mit Bäumen unter blauem Himmel"></section>
  <nav class="main-nav">
    <a class="is-active" style="left:211px">Home</a>
    <a style="left:283px">Über uns</a>
    <a style="left:344px">Katalog</a>
    <a style="left:418px">Verkaufen</a>
    <a style="left:482px">FAQ</a>
    <a style="left:544px">Kontakt</a>
    <a style="left:607px">Blog</a>
  </nav>
  <h1 class="hero-title">Wohnen heißt leben.</h1>

  <div class="grey-band"></div>

  <div class="tab tab--buy">Immobilie kaufen</div>
  <div class="tab tab--rent">Immobilie mieten<span class="caret"></span></div>
  <div class="tab tab--offer">Immobilie anbieten<span class="caret"></span></div>

  <form class="search-panel">
    <div class="search-field" style="top:20px">Immobilienart<span class="caret"></span></div>
    <div class="search-field" style="top:65px">Größe<span class="caret"></span></div>
    <div class="search-field" style="top:110px">Ort<span class="caret"></span></div>
    <div class="search-field" style="top:154px">Umkreis<span class="caret"></span></div>
    <div class="search-field" style="top:199px">Preis von<span class="caret"></span></div>
    <div class="search-field" style="top:244px">Weiteres<span class="caret"></span></div>
    <div class="search-submit">Suche<span class="pin"></span></div>
  </form>

  <div class="phone">030-55501234</div>
  <p class="contact-copy">Sie suchen eine Immobilie?<br>Sie möchten uns eine Immobilie anbieten?<br>Sprechen Sie mich an!</p>

  <div class="agent-photo" role="img" aria-label="Foto des Maklers im weißen Poloshirt mit Tablet-Tasche"></div>
</body>
</html>
```